Haunted Attraction Expert Website Design

A complete professional looking web site with 6 total pages.
Includes calendar and email form.
Needs to be word press and mobile user friendly.
Please use photos as labeled for the pages they will be presented on.
Company logo should alternate left and right sides of the page.
See attached layout for directions

Target Market(s)

Professionals, Haunted Attraction Owners/Operators

Industry/Entity Type

It Professional

Coding

Coded - Design and coding required

Number of Pages Required

5+ page

Font styles to use
Sans Serif

Colors

Designer to choose colors to be used in the design.

Requirements
Must have
• Our company logo on each page and photos supplied by me assigned to specific pages.
• Calendar
• Contact US Email Submission Form

```html
<!DOCTYPE html>
<html lang="en">
<head>
<meta charset="utf-8">
<title>Upcoming events – Fright Venue Advisors</title>
<link rel="stylesheet" href="https://fonts.googleapis.com/css2?family=Montserrat:ital,wght@0,400;0,500;0,700;1,400&display=swap">
<style>
  :root {
    --forest: #183d05;
    --nav-grey: #9a9c9e;
    --badge-grey: #a3a3a3;
    --orange: #f7941d;
    --white: #ffffff;
    --footer-bg: #1a2910;
    --footer-text: #b9bdb4;
  }
  * { margin: 0; padding: 0; box-sizing: border-box; }
  html, body { width: 872px; height: 1200px; overflow: hidden; }
  body {
    position: relative;
    background: var(--forest);
    font-family: "Montserrat", sans-serif;
    color: var(--white);
  }
  .site-header { position: absolute; left: 0; top: 0; width: 872px; height: 106px; }
  .brand {
    position: absolute; right: 102px; top: 40px;
    display: flex; align-items: center; gap: 7px;
    font-size: 14px; font-weight: 700; color: var(--orange);
  }
  .brand-mark { width: 12px; height: 12px; background: var(--orange); }
  .main-nav {
    position: absolute; left: 0; top: 106px; width: 872px; height: 55px;
    background: var(--nav-grey);
  }
  .main-nav a {
    position: absolute; top: 19px; font-size: 13px; color: var(--white);
    text-decoration: none; white-space: nowrap;
  }
  .main-nav a.current { font-weight: 700; }
  .event-calendar { position: absolute; left: 0; top: 0; width: 872px; height: 600px; }
  .event-row { position: absolute; left: 109px; top: 0; width: 600px; }
  .month {
    position: absolute; left: 0; top: var(--badge); width: 46px; height: 16px;
    background: var(--badge-grey); color: var(--orange);
    font-size: 12px; font-weight: 700; text-align: center; line-height: 16px;
  }
  .days, .details {
    position: absolute; top: var(--text); font-size: 14px; line-height: 14.5px; white-space: nowrap;
  }
  .days { left: 63px; }
  .details { left: 140px; }
  .feature-photo {
    position: absolute; left: 110px; top: 601px; width: 659px; height: 329px;
    background: linear-gradient(160deg, #e4e6e8 0%, #b7b2a4 45%, #7b6f5f 75%, #5a3b34 100%);
  }
  .testimonial { position: absolute; left: 137px; top: 1013px; }
  .quote-mark { position: absolute; left: 0; top: 0; }
  .quote-text {
    position: absolute; left: 68px; top: 21px; font-size: 20px; font-weight: 500;
    white-space: nowrap;
  }
  .quote-author {
    position: absolute; left: 68px; top: 58px; font-size: 15px; font-style: italic;
    white-space: nowrap;
  }
  .site-footer {
    position: absolute; left: 0; top: 1174px; width: 872px; height: 26px;
    background: var(--footer-bg);
  }
  .site-footer span {
    position: absolute; top: 7px; font-size: 10.5px; color: var(--footer-text); white-space: nowrap;
  }
</style>
</head>
<body>
  <header class="site-header">
    <div class="brand"><span class="brand-mark"></span>Fright Venue Advisors</div>
  </header>
  <nav class="main-nav">
    <a href="#" style="left:106px">Home</a>
    <a href="#" style="left:192px">About</a>
    <a href="#" style="left:278px">Consulting</a>
    <a href="#" style="left:392px">Expert Witnesses</a>
    <a href="#" class="current" style="left:544px">Upcoming events</a>
    <a href="#" style="left:703px">Contact Us</a>
  </nav>

  <main class="event-calendar">
    <div class="event-row" style="--badge:196px;--text:194px"><span class="month">JAN</span><span class="days">12 – 15<br>18 – 22</span><span class="details">New Orleans, Louisana<br>FORA Conference: San Diego, California</span></div>
    <div class="event-row" style="--badge:230px;--text:231px"><span class="month">FEB</span><span class="days">28</span><span class="details">Harvest Maze Expo: Chicago, Illinois</span></div>
    <div class="event-row" style="--badge:262px;--text:263px"><span class="month">MAR</span><span class="days">1 – 4</span><span class="details">Harvest Maze Expo: Chicago, Illinois</span></div>
    <div class="event-row" style="--badge:294px;--text:292px"><span class="month">APR</span><span class="days">13 – 15<br>20 – 22</span><span class="details">Pacific Coast Fright Expo: Portland, Oregon<br>Unavailable</span></div>
    <div class="event-row" style="--badge:326px;--text:324px"><span class="month">MAY</span><span class="days">3 – 6<br>21 – 29</span><span class="details">FORA Annual Conference: Clearwater, Florida<br>Heartland Scare Summit: Columbus, Ohio</span></div>
    <div class="event-row" style="--badge:358px;--text:361px"><span class="month">JUN</span><span class="days">20 – 26</span><span class="details">Grand Scream Tour: Ulster, New York</span></div>
    <div class="event-row" style="--badge:390px;--text:391px"><span class="month">JUL</span><span class="days">25 – 30</span><span class="details">Puzzle Room Summit: Nashville, Tennessee</span></div>
    <div class="event-row" style="--badge:422px;--text:423px"><span class="month">AUG</span><span class="days">26</span><span class="details">Creature Fest: Greely, Colorado</span></div>
    <div class="event-row" style="--badge:454px;--text:453px"><span class="month">SEP</span><span class="details">Unavailable</span></div>
    <div class="event-row" style="--badge:486px;--text:485px"><span class="month">OCT</span><span class="details">Unavailable</span></div>
    <div class="event-row" style="--badge:518px;--text:516px"><span class="month">NOV</span><span class="days">8 – 11<br>12 – 16</span><span class="details">Eerie Trail Tour: Orlando, Florida<br>ATEX: Orlando, Florida</span></div>
    <div class="event-row" style="--badge:550px;--text:552px"><span class="month">DEZ</span><span class="details">Will be announced soon</span></div>
  </main>

  <div class="feature-photo" role="img" aria-label="Photo of a weathered haunted manor facade with a snow-covered tree in front"></div>

  <blockquote class="testimonial">
    <svg class="quote-mark" width="42" height="32" viewBox="0 0 42 32" aria-hidden="true">
      <path d="M0 32 V18 C0 8 5 2 14 0 L16 4 C10 6 8 10 8 14 H17 V32 Z" fill="#fff"/>
      <path d="M23 32 V18 C23 8 28 2 37 0 L39 4 C33 6 31 10 31 14 H40 V32 Z" fill="#fff"/>
    </svg>
    <p class="quote-text">Doing the right thing daily, compounds over time.</p>
    <p class="quote-author">Samuel R. Whitford</p>
  </blockquote>

  <footer class="site-footer">
    <span style="left:247px">© 2018 Fright Venue Advisors</span>
    <span style="left:452px">Privacy Policy</span>
    <span style="left:550px">Terms of Service</span>
  </footer>
</body>
</html>
```